The Corvanta Group's website for high impact furniture promotions

I am looking for a simple website. we are a promotional company that runs events for furniture stores to increase sales for short periods of time. i would like the website to have about 4 areas to explain our company. I would like it to be simple and user friendly. I would like a link to chatterbook and a contact section. I am attaching our logo that i would like somewhere large or possibly in the backround. I am open to different color schemes. I would like to convey fast paced, modern, reliable. I am open to all different styles and look forward to seeing whats out there. we are looking for a quick turn around, so if we see one that we like quick, we will pick that one thanks
Updates
Project Deadline Extended
Reason: looking for some really creative designs and want to give a fair amount of time to produce
Target Market(s)
Retail Furniture store owners
Industry/Entity Type
It Company
Number of Pages Required
1 page
Colors
Designer to choose colors to be used in the design.
Look and feel
Each slider illustrates characteristics of the customer's brand and the style your logo design should communicate.

```html
<!DOCTYPE html>
<html lang="en">
<head>
<meta charset="utf-8">
<title>The Corvanta Group — High Impact Furniture Promotions</title>
<link rel="stylesheet" href="https://fonts.googleapis.com/css2?family=Montserrat:wght@600;700&family=Open+Sans:wght@400;600;700&display=swap">
<style>
:root{
  --tan:#c49a6c;
  --brown:#93603a;
  --band:#8e5c35;
  --ink:#222222;
  --text:#555555;
  --muted:#8a8a8a;
  --grey-bg:#ebebeb;
  --line:#dddddd;
  --white:#ffffff;
  --chat:#3b5998;
}
*{margin:0;padding:0;box-sizing:border-box}
html,body{width:1200px;height:3396px;overflow:hidden;background:var(--white)}
body{font-family:"Open Sans",Arial,sans-serif;color:var(--text);position:relative}
a{color:inherit;text-decoration:none}

/* header */
.site-header{position:absolute;left:0;top:0;width:1200px;height:155px;background:var(--white)}
.brand{position:absolute;left:150px;top:14px;width:180px;text-align:center}
.brand-disc{width:58px;height:58px;border-radius:50%;background:var(--tan);margin:0 auto 8px}
.brand-name{font-weight:600;font-size:17px;letter-spacing:2px;color:var(--brown);line-height:1.25;text-transform:uppercase}
.call{position:absolute;left:808px;top:30px;display:flex;align-items:center;gap:12px}
.round-btn{width:40px;height:40px;border-radius:50%;background:var(--brown);display:flex;align-items:center;justify-content:center}
.call-label{font-size:11px;font-weight:600;color:var(--ink);line-height:1.2;white-space:nowrap}
.call-number{font-size:21px;color:var(--brown);font-weight:600;line-height:1.1;white-space:nowrap}
.search{position:absolute;left:1026px;top:31px}
.main-nav{position:absolute;left:534px;top:108px;width:538px;height:47px;border-top:1px solid var(--line);display:flex;align-items:center;justify-content:space-between}
.main-nav a{font-size:11px;font-weight:700;color:var(--ink);height:46px;display:flex;align-items:center;padding:0 12px;white-space:nowrap}
.main-nav a.active{background:var(--tan);color:var(--white)}
.main-nav a:last-child{padding-right:0}

/* hero */
.hero{position:absolute;left:0;top:155px;width:1200px;height:560px}
.hero-photo{position:absolute;inset:0;background:linear-gradient(180deg,#e9e9e7 0%,#dedcd8 62%,#c9a27a 72%,#b8875a 100%)}
.hero-title{position:absolute;top:58px;width:100%;text-align:center;font-family:"Montserrat",Arial,sans-serif;font-weight:700;font-size:38px;color:var(--brown);letter-spacing:1px}
.hero-sub{position:absolute;top:110px;width:100%;text-align:center;font-size:16px;color:var(--ink)}
.btn{display:inline-block;background:var(--tan);color:var(--white);font-weight:700;text-transform:uppercase;white-space:nowrap}
.hero .btn{position:absolute;left:543px;top:151px;width:116px;height:30px;line-height:30px;text-align:center;font-size:15px}
.arrow{position:absolute;top:232px}

/* section headings */
.sec-title{position:absolute;width:100%;text-align:center;font-family:"Montserrat",Arial,sans-serif;font-weight:700;font-size:23px;color:var(--brown);letter-spacing:.5px}
.sec-rule{position:absolute;left:577px;width:46px;height:2px;background:var(--tan)}

/* welcome */
.welcome{position:absolute;left:0;top:715px;width:1200px;height:582px}
.welcome-intro{position:absolute;left:318px;top:145px;width:564px;text-align:center;font-size:12.5px;line-height:19px;color:var(--text)}
.features{position:absolute;left:0;top:265px;width:1200px}
.feature{position:absolute;width:210px;text-align:center}
.feature-icon{width:100px;height:100px;border-radius:50%;background:var(--tan);margin:0 auto;display:flex;align-items:center;justify-content:center}
.feature-name{margin-top:47px;font-size:12px;font-weight:700;color:var(--ink)}
.feature-text{margin-top:12px;font-size:11.5px;line-height:18px;color:var(--text);padding:0 28px}

/* events */
.events{position:absolute;left:0;top:1297px;width:1200px;height:444px;background:var(--grey-bg)}
.event-card{position:absolute;top:166px;width:226px;height:212px;background:var(--white);padding:26px 18px 0 22px}
.event-head{display:flex;gap:18px}
.event-marker{flex:none;width:16px;height:16px;background:var(--brown);margin-top:3px;display:flex;align-items:center;justify-content:center}
.event-title{font-size:13px;line-height:18px;color:var(--ink);font-weight:600}
.event-text{margin:16px 0 0 34px;font-size:11px;line-height:17px;color:var(--text)}
.event-card .btn{margin:14px 0 0 34px;font-size:9.5px;padding:4px 9px}

/* features band */
.promo{position:absolute;left:0;top:1741px;width:1200px;height:516px}
.promo-photo{position:absolute;inset:0;background:linear-gradient(180deg,#e4e4df 0%,#b9c0b4 34%,#7f8a70 50%,#6d5e4f 72%,#4e3f33 100%)}
.promo-kicker{position:absolute;top:50px;width:100%;text-align:center;font-size:14px;font-weight:700;color:var(--brown)}
.promo-text{position:absolute;top:86px;width:100%;text-align:center;font-size:20px;line-height:28px;color:#3a3a3a}
.promo .btn{position:absolute;left:565px;top:161px;font-size:10px;padding:5px 9px}

/* blog */
.blog{position:absolute;left:0;top:2257px;width:1200px;height:566px}
.post{position:absolute;top:156px;width:294px;height:354px;background:#f4f4f4;border:1px solid #e4e4e4;padding:16px 16px 0}
.post-photo{width:100%;height:181px}
.post-title{margin-top:18px;font-size:13px;line-height:19px;font-weight:700;color:var(--ink)}
.post-text{margin-top:8px;font-size:11px;line-height:17px;color:var(--text)}
.post .btn{margin-top:14px;font-size:9.5px;padding:4px 9px}

/* service strip */
.strip{position:absolute;left:0;top:2823px;width:1200px;height:188px;background:var(--band)}
.strip-item{position:absolute;top:45px;display:flex;gap:20px;color:var(--white)}
.strip-disc{flex:none;width:82px;height:82px;border-radius:50%;background:#dcc1a2;display:flex;align-items:center;justify-content:center}
.strip-title{font-size:13px;font-weight:700;text-transform:uppercase;margin-top:8px}
.strip-text{font-size:11px;line-height:16px;margin-top:6px;width:180px}
.strip-link{font-size:10px;font-weight:700;margin-top:6px;text-transform:uppercase}

/* footer */
.site-footer{position:absolute;left:0;top:3011px;width:1200px;height:385px}
.footer-brand{position:absolute;left:125px;top:50px;width:180px;text-align:center}
.social{position:absolute;left:190px;top:205px;display:flex;align-items:center;gap:8px;font-size:12px;color:var(--ink)}
.social-disc{width:32px;height:32px;border-radius:50%;background:var(--chat)}
.f-col{position:absolute;top:57px}
.f-head{font-size:11.5px;font-weight:700;color:var(--brown);text-transform:uppercase;margin-bottom:18px}
.f-list{list-style:none;font-size:11px;line-height:16.5px;color:var(--ink)}
.f-contact p{font-size:11px;line-height:16.5px;color:var(--ink);margin-bottom:14px}
.field{position:absolute;border:1px solid #cfcfcf;background:var(--white);font-size:10px;color:var(--ink);padding:7px 10px}
.submit{position:absolute;left:772px;top:3215px;width:68px;height:30px;background:var(--brown);color:var(--white);font-size:9.5px;font-weight:700;text-align:center;line-height:30px}
.footer-rule{position:absolute;left:132px;top:3300px;width:936px;height:1px;background:var(--line)}
.copyright{position:absolute;left:132px;top:3336px;font-size:11px;color:var(--ink)}
</style>
</head>
<body>

<header class="site-header">
  <div class="brand">
    <div class="brand-disc"></div>
    <div class="brand-name">The Corvanta Group</div>
  </div>
  <div class="call">
    <span class="round-btn">
      <svg width="16" height="16" viewBox="0 0 24 24" fill="#fff"><path d="M6.6 10.8a15 15 0 006.6 6.6l2.2-2.2c.3-.3.7-.4 1-.2 1.1.4 2.3.6 3.6.6.6 0 1 .4 1 1V20c0 .6-.4 1-1 1A17 17 0 013 4c0-.6.4-1 1-1h3.5c.6 0 1 .4 1 1 0 1.3.2 2.5.6 3.6.1.3 0 .7-.2 1z"/></svg>
    </span>
    <div>
      <div class="call-label">CALL US NOW</div>
      <div class="call-number">555.014.2290</div>
    </div>
  </div>
  <span class="round-btn search">
    <svg width="16" height="16" viewBox="0 0 24 24" fill="none" stroke="#fff" stroke-width="3"><circle cx="10" cy="10" r="6"/><path d="M15 15l5 5"/></svg>
  </span>
  <nav class="main-nav">
    <a class="active" href="#">HOME</a>
    <a href="#">ABOUT US</a>
    <a href="#">EVENTS</a>
    <a href="#">SERVICES</a>
    <a href="#">BLOG</a>
    <a href="#">CONTACT US</a>
  </nav>
</header>

<section class="hero">
  <div class="hero-photo" role="img" aria-label="Living room with a wooden console table, lamp, vases and a grey armchair on a wood floor"></div>
  <h1 class="hero-title">FURNITURE</h1>
  <p class="hero-sub">Lorem Ipsum is simply dummy text of the printing</p>
  <a class="btn" href="#">Read More</a>
  <svg class="arrow" style="left:40px" width="22" height="40" viewBox="0 0 22 40"><path d="M18 4L4 20l14 16" fill="none" stroke="#222" stroke-width="3.5"/></svg>
  <svg class="arrow" style="left:1138px" width="22" height="40" viewBox="0 0 22 40"><path d="M4 4l14 16L4 36" fill="none" stroke="#222" stroke-width="3.5"/></svg>
</section>

<section class="welcome">
  <h2 class="sec-title" style="top:62px">WELCOME TO OUR SITE</h2>
  <div class="sec-rule" style="top:115px"></div>
  <p class="welcome-intro">There are many variations of passages of Lorem Ipsum available, but the majority have suffered alteration in some form, by injected humour, or randomised words which don't look even believable. If you are going to use a passage of Lorem Ipsum, you.</p>
  <div class="features">
    <div class="feature" style="left:115px">
      <div class="feature-icon"><svg width="28" height="28" viewBox="0 0 24 24" fill="none" stroke="#fff" stroke-width="2"><rect x="3" y="5" width="18" height="16" rx="1"/><path d="M3 10h18M8 3v4M16 3v4"/></svg></div>
      <div class="feature-name">EVENT EXPERIENCED</div>
      <p class="feature-text">There are many variations of passages of Lorem Ipsum available, but the majority have suffered alteration.</p>
    </div>
    <div class="feature" style="left:352px">
      <div class="feature-icon"><svg width="30" height="28" viewBox="0 0 30 24" fill="#fff"><circle cx="15" cy="7" r="4"/><circle cx="6" cy="9" r="3"/><circle cx="24" cy="9" r="3"/><path d="M8 22c0-5 3-8 7-8s7 3 7 8zM0 21c0-4 2-7 6-7 1 0 2 .3 2.5.7C7 16 6.5 18 6.5 21zM30 21c0-4-2-7-6-7-1 0-2 .3-2.5.7C23 16 23.5 18 23.5 21z"/></svg></div>
      <div class="feature-name">EXPERIENCE TEAM</div>
      <p class="feature-text">There are many variations of passages of Lorem Ipsum available, but the majority have suffered alteration.</p>
    </div>
    <div class="feature" style="left:624px">
      <div class="feature-icon"><svg width="28" height="28" viewBox="0 0 24 24" fill="#fff"><rect x="2" y="10" width="4" height="11"/><path d="M8 10l4-8c1.5 0 2.5 1 2.5 2.5L14 9h6c1 0 2 1 1.8 2l-1.5 8c-.2 1-1 2-2 2H8z"/></svg></div>
      <div class="feature-name">QUALITY</div>
      <p class="feature-text">There are many variations of passages of Lorem Ipsum available, but the majority have suffered alteration.</p>
    </div>
    <div class="feature" style="left:882px">
      <div class="feature-icon"><svg width="28" height="28" viewBox="0 0 24 24" fill="none" stroke="#fff" stroke-width="2.2"><path d="M4 15v-3a8 8 0 0116 0v3"/><rect x="3" y="14" width="4" height="6" rx="1" fill="#fff"/><rect x="17" y="14" width="4" height="6" rx="1" fill="#fff"/></svg></div>
      <div class="feature-name">SUPPORT</div>
      <p class="feature-text">There are many variations of passages of Lorem Ipsum available, but the majority have suffered alteration.</p>
    </div>
  </div>
</section>

<section class="events">
  <h2 class="sec-title" style="top:52px">EVENTS</h2>
  <div class="sec-rule" style="top:99px"></div>
  <article class="event-card" style="left:131px">
    <div class="event-head"><span class="event-marker"><svg width="6" height="8" viewBox="0 0 6 8"><path d="M0 0l6 4-6 4z" fill="#fff"/></svg></span><h3 class="event-title">Lorem Ipsum is simply dummy text</h3></div>
    <p class="event-text">There are many variations of passages of Lorem Ipsum available, but the majority have...</p>
    <a class="btn" href="#">Read More</a>
  </article>
  <article class="event-card" style="left:368px">
    <div class="event-head"><span class="event-marker"><svg width="6" height="8" viewBox="0 0 6 8"><path d="M0 0l6 4-6 4z" fill="#fff"/></svg></span><h3 class="event-title">There are many variation s of passages</h3></div>
    <p class="event-text">There are many variations of passages of Lorem Ipsum available, but the majority have...</p>
    <a class="btn" href="#">Read More</a>
  </article>
  <article class="event-card" style="left:605px">
    <div class="event-head"><span class="event-marker"><svg width="6" height="8" viewBox="0 0 6 8"><path d="M0 0l6 4-6 4z" fill="#fff"/></svg></span><h3 class="event-title">Handful of model sente nce structures</h3></div>
    <p class="event-text">There are many variations of passages of Lorem Ipsum available, but the majority have...</p>
    <a class="btn" href="#">Read More</a>
  </article>
  <article class="event-card" style="left:842px">
    <div class="event-head"><span class="event-marker"><svg width="6" height="8" viewBox="0 0 6 8"><path d="M0 0l6 4-6 4z" fill="#fff"/></svg></span><h3 class="event-title">Lorem Ipsum is simply dummy text</h3></div>
    <p class="event-text">There are many variations of passages of Lorem Ipsum available, but the majority have...</p>
    <a class="btn" href="#">Read More</a>
  </article>
</section>

<section class="promo">
  <div class="promo-photo" role="img" aria-label="Outdoor terrace lounge set with sofa, armchairs and ottomans overlooking misty mountains"></div>
  <div class="promo-kicker">FEATURES</div>
  <p class="promo-text">It is a long established fact that a lorem isujm<br>reader will be distracted</p>
  <a class="btn" href="#">Read More</a>
</section>

<section class="blog">
  <h2 class="sec-title" style="top:58px">LATEST BLOG</h2>
  <div class="sec-rule" style="top:104px"></div>
  <article class="post" style="left:136px">
    <div class="post-photo" role="img" aria-label="Bright living room with a grey sectional sofa" style="background:linear-gradient(180deg,#e6e4e1,#bdb7b0)"></div>
    <h3 class="post-title">Lorem Ipsum is simply dummy text of the printing</h3>
    <p class="post-text">Contrary to popular belief, Lorem Ipsum is not simply random text. It has roots.</p>
    <a class="btn" href="#">Read More</a>
  </article>
  <article class="post" style="left:453px">
    <div class="post-photo" role="img" aria-label="Patio with red cushioned wooden chairs" style="background:linear-gradient(180deg,#8a9a6a,#b5513f 60%,#8b6a48)"></div>
    <h3 class="post-title">There are many variations of passages of Lorem Ipsum available</h3>
    <p class="post-text">Contrary to popular belief, Lorem Ipsum is not simply random text. It has roots.</p>
    <a class="btn" href="#">Read More</a>
  </article>
  <article class="post" style="left:772px">
    <div class="post-photo" role="img" aria-label="Modern dining room with table and chairs under pendant lights" style="background:linear-gradient(180deg,#ecebe8,#c9c2b8)"></div>
    <h3 class="post-title">It is a long established fact that a reader will be distracted</h3>
    <p class="post-text">Contrary to popular belief, Lorem Ipsum is not simply random text. It has roots.</p>
    <a class="btn" href="#">Read More</a>
  </article>
</section>

<section class="strip">
  <div class="strip-item" style="left:133px">
    <span class="strip-disc"><svg width="30" height="30" viewBox="0 0 24 24" fill="#fff"><path d="M12 8a4 4 0 100 8 4 4 0 000-8zm9 5.5v-3l-2.4-.5-.7-1.7 1.3-2-2.1-2.1-2 1.3-1.7-.7L13 2.5h-3l-.5 2.4-1.7.7-2-1.3L3.7 6.4l1.3 2-.7 1.7-2.3.4v3l2.4.5.7 1.7-1.3 2 2.1 2.1 2-1.3 1.7.7.5 2.4h3l.5-2.4 1.7-.7 2 1.3 2.1-2.1-1.3-2 .7-1.7z"/></svg></span>
    <div><div class="strip-title">Our Services</div><p class="strip-text">Contrary to popular belief, Lorem Ipsum is not simply random a</p><div class="strip-link">Read More</div></div>
  </div>
  <div class="strip-item" style="left:477px">
    <span class="strip-disc"></span>
    <div><div class="strip-title">About Us</div><p class="strip-text">Contrary to popular belief, Lorem Ipsum is not simply random a</p><div class="strip-link">Read More</div></div>
  </div>
  <div class="strip-item" style="left:810px">
    <span class="strip-disc"><svg width="24" height="32" viewBox="0 0 24 32" fill="#fff"><path d="M12 0C5.4 0 0 5.2 0 11.7 0 20 12 32 12 32s12-12 12-20.3C24 5.2 18.6 0 12 0zm0 16a4.5 4.5 0 110-9 4.5 4.5 0 010 9z"/></svg></span>
    <div><div class="strip-title">Our Locations</div><p class="strip-text">Contrary to popular belief, Lorem Ipsum is not simply random a</p><div class="strip-link">Read More</div></div>
  </div>
</section>

<footer class="site-footer">
  <div class="footer-brand">
    <div class="brand-disc"></div>
    <div class="brand-name">The Corvanta Group</div>
  </div>
  <a class="social" href="#"><span class="social-disc"></span>chatterbook</a>
  <div class="f-col" style="left:403px">
    <div class="f-head">Menu</div>
    <ul class="f-list"><li>Home</li><li>About us</li><li>Services</li><li>Events</li><li>Blog</li><li>Contact us</li></ul>
  </div>
  <div class="f-col f-contact" style="left:573px">
    <div class="f-head">Contact Us</div>
    <p>1180 Alder Crest Lane<br>Pine Harbor, MI 48000</p>
    <p>555.014.2290</p>
    <p>info@thecorvanta.com</p>
  </div>
  <div class="f-col" style="left:772px">
    <div class="f-head">Quick Contact</div>
  </div>
</footer>
<div class="field" style="left:772px;top:3104px;width:140px;height:30px">Name</div>
<div class="field" style="left:926px;top:3104px;width:140px;height:30px">E mail id</div>
<div class="field" style="left:772px;top:3145px;width:294px;height:60px">Message</div>
<div class="submit">SUBMIT</div>
<div class="footer-rule"></div>
<div class="copyright">Copyrights @ 2017 All Rights Reserved</div>

</body>
</html>
```